Blue Heron Courier & Delivery Services needs a flyer

We need an introductory flyer for a new company based in Yellowknife, Northwest Territories,Canada. Our company name is Blue Heron Courier & Delivery Services. We will be handling envelopes and small packages up to 20 pounds. We expect 20 percent of our business to come from residential customers and 80 percent from the business community including lawyers, doctors, engineers and government offices. The main message that we will try to convey in this flyer is that we are a new and exciting company that promises to make 100% customer satisfaction our number one goal. I would like the layout to be elegant and simple and certainly not cluttered. It will be a single sided flyer. Text should be easy to read and most likely at most two fonts. I would like one stunning image or photo relating to the courier business and message. There should be plenty of white space throughout the flyer and nice margins on all sides. I would like my flyer to be 8.5 inches by 11 inches and it should read from top to bottom. . I would like a nice big bold headline that in some way mentions " Special Offer- Up to 100% Off. You can change the wording if you have a better idea. Throughout the flyer you can highlight and italicize for emphasis. Please try to use bullet points for my five main reasons for hiring our company which are: you will be 100% satisfied with each delivery or you will be given a complete refund no questions asked, your envelope or package will be delivered on time every time, you will always be treated throughout the delivery process in a professional manner, you will be given the widest selection in Yellowknife of price points and delivery options , you can trust us with your most important and time sensitive deliveries. Try to incorporate something next to these five points to really draw attention like a check mark, star etc.... I would prefer if my company name and contact info is in the bottom third of the flyer. My email is blueheroncourieryk@mailbox-example.net. My phone number is 867-312-7794. It might be a good idea to have my phone number also at the top of the flyer someplace after the headline saying like Call Now!!! you can use boxes, borders and contrasting bold colors to bring flyer to life. I have a testimonial from a business owner that I dealt with when I ran another business which would be nice to have included . " While receiving daily deliveries for 18 years from Calvin Marsh I found him to be punctual , reliable and efficient " Glen Potter, owner of Potter and Lindqvist Trading LTD, Yellowknife,NWT. I thought perhaps at the top of flyer after the headline perhaps in some way you could say Yellowknife's newest and best courier and delivery service is pleased to offer the following stunning discounts: then you could list the three special offers: 1) First 5 businesses to book regular scheduled deliveries will get 100% off their first delivery. 2) First 5 businesses to book a single delivery will get 50% off that delivery. 3) First 5 residential customers to book a delivery will receive 25% off that delivery. I thought you could mention my name somewhere. Calvin Marsh. Owner has lived in Yellowknife for 42 years and has 20 years experience doing performing important and time sensitive deliveries. Perhaps you could mention somewhere that we will have a couple of ongoing discounts also which will be 1) seniors discounts. 2) regular scheduled deliveries discounts. I have suggested colors but if you have other ideas I would certainly look at them. Our business tag line is. On Time Every Time
Target Market(s)
Business owners typically males 30-50 years old
Industry/Entity Type
Delivery Service
Requirements
Must have
- Done in CMYK mode sufficient bleed size for printing
Nice to have
- Nothing set in stone. I recently had my logo design uploaded to this brief. It is up to you if you feel it should be included in the flyer.
Should not have
- I am willing to look at any design

```html
<!DOCTYPE html>
<html lang="en">
<head>
<meta charset="utf-8">
<title>Blue Heron Courier &amp; Delivery Services – Flyer</title>
<link rel="stylesheet" href="https://fonts.googleapis.com/css2?family=Cinzel:wght@400;700;900&family=Source+Sans+3:ital,wght@0,400;0,600;0,700;1,700&display=swap">
<style>
  :root {
    --page-bg: #dfe2e6;
    --brand-blue: #1a6fb5;
    --ink: #1f2a36;
    --band-blue: #0b79bf;
    --band-navy: #123f60;
    --footer-navy: #0f4468;
    --ribbon-red: #d8232a;
    --ribbon-dark: #c01c22;
    --ribbon-fold: #8a1014;
    --peach: rgba(243, 206, 182, 0.78);
    --quote-grey: #7b7b7b;
    --badge-orange: #ef7d1a;
    --sky-top: #eaf3fa;
  }
  * { box-sizing: border-box; margin: 0; padding: 0; }
  html, body {
    width: 1025px; height: 1200px; overflow: hidden;
    background: var(--page-bg);
    font-family: "Source Sans 3", Arial, sans-serif;
    color: var(--ink);
  }
  .flyer {
    position: absolute; left: 64px; top: 18px;
    width: 897px; height: 1164px;
    background: linear-gradient(180deg, var(--sky-top) 0%, #f6fafd 38%, #ffffff 55%);
    overflow: hidden;
    box-shadow: 0 4px 18px rgba(0,0,0,0.18);
  }
  .hero-road, .hero-courier { position: absolute; }
  .hero-road {
    left: 0; top: 60px; width: 300px; height: 450px;
    background: linear-gradient(90deg, rgba(150,165,180,0.45) 0%, rgba(200,210,220,0.35) 60%, rgba(234,243,250,0) 100%);
  }
  .hero-courier {
    left: 695px; top: 232px; width: 202px; height: 255px;
    background: linear-gradient(160deg, #bcd6ee 0%, #2f6fb9 55%, #d8b88d 100%);
    opacity: 0.9;
  }
  .brand-name {
    position: absolute; left: 200px; top: 40px; width: 560px;
    text-align: center;
    font-family: "Cinzel", "Times New Roman", serif; font-weight: 700;
    font-size: 62px; line-height: 76px; color: var(--brand-blue); letter-spacing: 1px;
  }
  .brand-sub {
    position: absolute; left: 180px; top: 112px; width: 600px;
    text-align: center;
    font-family: "Cinzel", "Times New Roman", serif; font-weight: 400;
    font-size: 31px; line-height: 38px; color: var(--ink); letter-spacing: 0.5px;
  }
  .brand-scope {
    position: absolute; left: 200px; top: 154px; width: 560px;
    text-align: center; font-size: 14px; color: var(--ink);
  }
  .top-phone {
    position: absolute; left: 268px; top: 185px;
    display: flex; align-items: center; gap: 12px;
    font-size: 42px; font-weight: 700; color: var(--ink);
  }
  .top-phone svg { width: 52px; height: 44px; }
  .testimonial {
    position: absolute; left: 247px; top: 264px; width: 392px; height: 178px;
    background: var(--peach); border-radius: 6px;
    padding: 38px 24px 0; text-align: center;
  }
  .testimonial-mark {
    position: absolute; left: 250px; top: 222px;
    font-family: Georgia, serif; font-size: 130px; line-height: 1;
    color: var(--quote-grey); font-weight: 700;
  }
  .testimonial-text { font-size: 17px; line-height: 22px; color: var(--ink); }
  .testimonial-author { margin-top: 8px; font-size: 14px; line-height: 17px; color: var(--ink); }
  .satisfaction-badge { position: absolute; left: 596px; top: 374px; width: 174px; height: 98px; }
  .intro-headline {
    position: absolute; left: 0; top: 503px; width: 897px;
    text-align: center; font-size: 25px; line-height: 32px; font-weight: 400;
    text-transform: uppercase; color: var(--ink);
  }
  .offer-ribbon { position: absolute; left: 108px; top: 580px; width: 692px; height: 70px; }
  .offer-ribbon-text {
    position: absolute; left: 108px; top: 590px; width: 692px;
    text-align: center; font-family: "Cinzel", "Times New Roman", serif;
    font-weight: 700; font-size: 28px; line-height: 38px; color: #ffffff;
  }
  .offer-list {
    position: absolute; left: 120px; top: 660px; list-style: none;
    font-size: 17px; line-height: 30px; color: var(--ink);
  }
  .why-band {
    position: absolute; left: 0; top: 767px; width: 897px; height: 254px;
    background: var(--band-blue);
  }
  .why-title {
    position: absolute; left: 0; top: 765px; width: 215px; height: 62px;
    background: var(--band-navy); color: #fff; font-weight: 400;
    font-size: 40px; line-height: 62px; text-align: center;
  }
  .owner-note {
    position: absolute; left: 228px; top: 773px; width: 650px;
    font-size: 16px; line-height: 20px; color: #fff;
  }
  .owner-name { font-weight: 700; font-style: italic; font-size: 21px; }
  .reasons {
    position: absolute; left: 45px; top: 845px; list-style: none;
    font-size: 16.5px; color: #fff;
  }
  .reasons li { display: flex; align-items: center; height: 31px; gap: 14px; }
  .reasons svg { width: 28px; height: 26px; flex: none; }
  .band-rule { position: absolute; left: 0; top: 1021px; width: 897px; height: 2px; background: #cfe3f2; }
  .contact-footer {
    position: absolute; left: 0; top: 1023px; width: 897px; height: 141px;
    background: linear-gradient(180deg, #14507a 0%, var(--footer-navy) 100%);
    color: #fff; text-align: center;
  }
  .contact-email { margin-top: 18px; font-size: 20px; }
  .contact-call { margin-top: 8px; font-size: 44px; font-weight: 700; }
</style>
</head>
<body>
<main class="flyer">
  <div class="hero-road" role="img" aria-label="Photo of a highway rising upward into an arrow"></div>
  <div class="hero-courier" role="img" aria-label="Photo of a courier in a blue uniform and cap holding a cardboard parcel"></div>

  <h1 class="brand-name">BLUE HERON</h1>
  <p class="brand-sub">COURIER &amp; DELIVERY SERVICES</p>
  <p class="brand-scope">We will be handling envelopes and small packages up to 20 pounds</p>

  <div class="top-phone">
    <svg viewBox="0 0 52 44" aria-hidden="true">
      <path d="M4 14 C4 4 48 4 48 14 L48 18 L38 18 L36 12 C30 10 22 10 16 12 L14 18 L4 18 Z" fill="#1a7fc4"/>
      <path d="M12 20 L18 15 L34 15 L40 20 L46 40 L6 40 Z" fill="#1a7fc4"/>
      <circle cx="26" cy="28" r="6" fill="#ffffff"/>
      <circle cx="26" cy="28" r="3" fill="#1a7fc4"/>
    </svg>
    <span>867-312-7794</span>
  </div>

  <div class="testimonial">
    <p class="testimonial-text">While receiving daily deliveries for 18 years from Calvin Marsh I found him to be punctual ,<br>reliable and efficient "</p>
    <p class="testimonial-author">Glen Potter,<br>owner of Potter and Lindqvist Trading LTD,<br>Yellowknife,NWT.</p>
  </div>
  <div class="testimonial-mark" aria-hidden="true">&ldquo;</div>

  <svg class="satisfaction-badge" viewBox="0 0 174 98" aria-label="100% customer satisfaction is our number one goal">
    <polygon points="22,4 152,4 172,49 152,94 22,94 2,49" fill="#ffffff" stroke="#f2a55e" stroke-width="3"/>
    <text x="87" y="28" text-anchor="middle" font-family="Source Sans 3, sans-serif" font-size="15" fill="#333"><tspan fill="#ef7d1a" font-weight="700">100%</tspan> CUSTOMER</text>
    <rect x="-2" y="36" width="178" height="30" fill="#ef7d1a"/>
    <text x="87" y="58" text-anchor="middle" font-family="Source Sans 3, sans-serif" font-size="21" font-weight="700" font-style="italic" fill="#ffffff">SATISFACTION</text>
    <text x="87" y="80" text-anchor="middle" font-family="Source Sans 3, sans-serif" font-size="9" fill="#333">IS OUR NUMBER ONE GOAL</text>
  </svg>

  <h2 class="intro-headline">Yellowknife's newest and best courier and delivery<br>service is pleased to offer the following stunning discounts</h2>

  <svg class="offer-ribbon" viewBox="0 0 692 70" aria-hidden="true">
    <polygon points="0,8 60,8 60,52 0,52 14,30" fill="var(--ribbon-dark)"/>
    <polygon points="692,8 632,8 632,52 692,52 678,30" fill="var(--ribbon-dark)"/>
    <polygon points="44,52 60,52 60,62" fill="var(--ribbon-fold)"/>
    <polygon points="648,52 632,52 632,62" fill="var(--ribbon-fold)"/>
    <rect x="44" y="0" width="604" height="58" fill="var(--ribbon-red)"/>
  </svg>
  <p class="offer-ribbon-text">SPECIAL OFFERS- UP TO 100% OFF.</p>

  <ol class="offer-list">
    <li>1) First 5 businesses to book regular scheduled deliveries will get 100% off their first delivery.</li>
    <li>2) First 5 businesses to book a single delivery will get 50% off that delivery.</li>
    <li>3) First 5 residential customers to book a delivery will receive 25% off that delivery.</li>
  </ol>

  <section>
    <div class="why-band"></div>
    <h2 class="why-title">WHY US</h2>
    <p class="owner-note"><span class="owner-name">Calvin Marsh.</span> Owner has lived in Yellowknife for 42 years and has 20 years experience doing performing important and time sensitive deliveries.</p>
    <ul class="reasons">
      <li><svg viewBox="0 0 28 26" aria-hidden="true"><path d="M2 14 L10 22 L26 3 L22 1 L10 15 L6 10 Z" fill="#ffffff"/></svg>You will be given a complete refund no questions asked</li>
      <li><svg viewBox="0 0 28 26" aria-hidden="true"><path d="M2 14 L10 22 L26 3 L22 1 L10 15 L6 10 Z" fill="#ffffff"/></svg>Your envelope or package will be delivered on time every time</li>
      <li><svg viewBox="0 0 28 26" aria-hidden="true"><path d="M2 14 L10 22 L26 3 L22 1 L10 15 L6 10 Z" fill="#ffffff"/></svg>You will always be treated throughout the delivery process in a professional manner</li>
      <li><svg viewBox="0 0 28 26" aria-hidden="true"><path d="M2 14 L10 22 L26 3 L22 1 L10 15 L6 10 Z" fill="#ffffff"/></svg>You will be given the widest selection in Yellowknife of price points and delivery options</li>
      <li><svg viewBox="0 0 28 26" aria-hidden="true"><path d="M2 14 L10 22 L26 3 L22 1 L10 15 L6 10 Z" fill="#ffffff"/></svg>You can trust us with your most important and time sensitive deliveries</li>
    </ul>
    <div class="band-rule"></div>
  </section>

  <footer class="contact-footer">
    <p class="contact-email">blueheroncourieryk@mailbox-example.net</p>
    <p class="contact-call">Call Us Now&nbsp; 867-312-7794</p>
  </footer>
</main>
</body>
</html>
```